Business Card Design

Professional solutions in (servers, security, networks, programming)

Industry/Entity Type

Business

Contact Information for Business Card

Nadim Fouzan
Internet services and network solutions
TDK - GLPW - GLPT
netdesk@kavo-lin.com / 05291473806
www.kavo-lin.com

```html
<!DOCTYPE html>
<html lang="en">
<head>
<meta charset="utf-8">
<title>Nadim Fouzan — Business Card</title>
<link rel="stylesheet" href="https://fonts.googleapis.com/css2?family=Lato:ital,wght@0,700;0,900;1,700&display=swap">
<style>
  :root {
    --backdrop: #2a2a2a;
    --card: #f7f7f7;
    --card-edge: #e6e6e6;
    --green: #78b833;
    --green-dark: #5e9a22;
    --grey: #7a7a7a;
    --ink: #151515;
  }
  * { box-sizing: border-box; margin: 0; padding: 0; }
  html, body {
    width: 1200px;
    height: 873px;
    overflow: hidden;
    background: var(--backdrop);
    font-family: "Lato", Arial, sans-serif;
  }
  .stage {
    width: 1200px;
    height: 873px;
    display: flex;
    align-items: center;
    justify-content: center;
  }
  .business-card {
    position: relative;
    width: 900px;
    height: 514px;
    background: linear-gradient(135deg, #ffffff 0%, var(--card) 55%, var(--card-edge) 100%);
    box-shadow: 0 18px 40px rgba(0, 0, 0, 0.55);
    display: flex;
    align-items: center;
    justify-content: center;
    gap: 28px;
  }
  .identity {
    text-align: right;
    display: flex;
    flex-direction: column;
    align-items: flex-end;
    gap: 4px;
    padding-top: 34px;
  }
  .identity__name {
    color: var(--green);
    font-weight: 900;
    font-size: 28px;
    letter-spacing: 0.5px;
    text-transform: uppercase;
  }
  .identity__tagline {
    color: var(--grey);
    font-style: italic;
    font-weight: 700;
    font-size: 21px;
  }
  .identity__certs {
    color: var(--ink);
    font-weight: 900;
    font-size: 23px;
    margin-top: 2px;
  }
  .divider {
    width: 4px;
    height: 120px;
    background: linear-gradient(to bottom, rgba(120, 184, 51, 0) 0%, var(--green) 45%, rgba(120, 184, 51, 0) 100%);
  }
  .contacts {
    list-style: none;
    display: flex;
    flex-direction: column;
    gap: 14px;
    padding-bottom: 12px;
  }
  .contacts__item {
    display: flex;
    align-items: center;
    gap: 14px;
    color: var(--ink);
    font-weight: 700;
    font-size: 20px;
  }
  .contacts__icon {
    width: 28px;
    height: 28px;
    flex: none;
  }
</style>
</head>
<body>
<main class="stage">
  <section class="business-card" aria-label="Business card for Nadim Fouzan">
    <div class="identity">
      <h1 class="identity__name">Nadim Fouzan</h1>
      <p class="identity__tagline">Internet services and network solutions</p>
      <p class="identity__certs">TDK - GLPW - GLPT</p>
    </div>
    <div class="divider" aria-hidden="true"></div>
    <ul class="contacts">
      <li class="contacts__item">
        <svg class="contacts__icon" viewBox="0 0 28 28" aria-hidden="true">
          <circle cx="14" cy="14" r="14" fill="var(--green)"/>
          <path d="M9.5 7.5c.8-.6 1.8-.4 2.2.4l1.2 2.3c.3.7.1 1.4-.5 1.8l-.9.6c.7 1.6 1.9 2.9 3.5 3.7l.6-.9c.4-.6 1.2-.8 1.8-.4l2.2 1.3c.8.5 1 1.5.4 2.2l-.9 1.1c-.6.7-1.6 1-2.5.7-4-1.4-7-4.4-8.3-8.4-.3-.9 0-1.9.7-2.5z" fill="#fff"/>
        </svg>
        <span>05291473806</span>
      </li>
      <li class="contacts__item">
        <svg class="contacts__icon" viewBox="0 0 28 28" aria-hidden="true">
          <circle cx="14" cy="14" r="14" fill="var(--green)"/>
          <rect x="7" y="9" width="14" height="10" rx="1.2" fill="#fff"/>
          <path d="M7.6 9.6 14 14.6l6.4-5" fill="none" stroke="var(--green)" stroke-width="1.4"/>
        </svg>
        <span>netdesk@kavo-lin.com</span>
      </li>
      <li class="contacts__item">
        <svg class="contacts__icon" viewBox="0 0 28 28" aria-hidden="true">
          <circle cx="14" cy="14" r="14" fill="var(--green)"/>
          <g fill="none" stroke="#fff" stroke-width="2" stroke-linecap="round">
            <path d="M12.5 15.5l-2 2a2.4 2.4 0 0 1-3.4-3.4l2.5-2.5a2.4 2.4 0 0 1 3.4 0"/>
            <path d="M15.5 12.5l2-2a2.4 2.4 0 0 1 3.4 3.4l-2.5 2.5a2.4 2.4 0 0 1-3.4 0"/>
          </g>
        </svg>
        <span>www.kavo-lin.com</span>
      </li>
    </ul>
  </section>
</main>
</body>
</html>
```